In-product message pop-up (to upsell software users to paid WHILE using software)

We need an IRRESISTIBLY CLICKABLE pop-up window to present to Windows desktop users of our software security suite. The pop-up will be presented to active users of Korvel's Trailmute software with the ultimate goal of UPSELLING them to buy Korvel's premium product called "VaultSweep" which helps users to scan and remove their data from the darkweb. https://www.korvelsoft.example/en-us/vaultsweep Some FAILED pop-ups are attached as images. The words of these pop-ups are fine, but we need 5X better results than these tests. Please STUDY what the team has ALREADY tried, and think of a message and design that is MORE COMPELLING for users of an anti-track software to CLICK ON in regards to protecting themselves from compromised email/passwords/personal information being leaked by hackers. You only have room for a few words and 1-2 sentences. Think! The best design that will maximize clicks while complying with the corporate style of Korvelsoft.example will win!

Target Market(s)

U.S. users of VPN and anti-track/anti-cookie software

Industry/Entity Type

Computer Software

Font styles to use
Sans Serif

Requirements
Must have
• Acceptable sizes: 728X90, 300X250, or 300X600. Follow the color scheme of Korvel. https://www.korvelsoft.example/en-us/about The message must
Nice to have
• Follow the corporate look n' feel of Korvel. But think CREATIVELY about how to convince someone who is using Korvel's free software to CLICK on the pop-up while they're using their desktop and LEARN about VaultSweep https://findlumen.example/?q=korvel&t=osx&iax=images&ia=images Again we are advertising "VaultSweep" which helps users to remove their personal data from the darkweb and prevent data breaches. But your pop-up shouldn't reference VaultSweep specifically, it should just maximize clicks about something that appeals to the user, in a way that relates to VaultSweep's value proposition (protect yourself, remove your data, scan your email, resolve security concerns, etc.)
Should not have
• Nothing that Korvel corporate won't approve (pornography, profanity, risqué photos, sensational language, etc.)

```html
<!DOCTYPE html>
<html lang="en">
<head>
<meta charset="utf-8">
<title>Korvel – Email exposure check pop-up</title>
<link rel="stylesheet" href="https://fonts.googleapis.com/css2?family=Roboto:wght@400;500;700&display=swap">
<style>
  :root {
    --canvas-bg: #f1f1f1;
    --popup-bg: #3b4153;
    --popup-edge: #2f3443;
    --text-main: #ffffff;
    --text-muted: #a7adbd;
    --text-accent: #ffb37a;
    --badge-bg: #7b5cf0;
    --brand-dot: #ff7a1a;
    --cta-bg: #4fb35c;
    --cta-edge: #6cc978;
    --icon-ring: #8a3a4e;
    --icon-fill: #4a4f63;
    --close: #c9cdd8;
  }
  * { box-sizing: border-box; margin: 0; padding: 0; }
  html, body {
    width: 1200px;
    height: 807px;
    overflow: hidden;
    background: var(--canvas-bg);
    font-family: "Roboto", Arial, sans-serif;
  }
  .stage {
    width: 1200px;
    height: 807px;
    display: flex;
    align-items: center;
    justify-content: center;
  }
  .popup {
    position: relative;
    width: 728px;
    height: 90px;
    background: var(--popup-bg);
    border: 1px solid var(--popup-edge);
    transform: scale(1.5);
    color: var(--text-main);
  }
  .popup__icon {
    position: absolute;
    left: 34px;
    top: 15px;
    width: 60px;
    height: 60px;
    border-radius: 50%;
    background: radial-gradient(circle at 50% 45%, var(--icon-fill), var(--popup-bg) 70%);
    border: 1.5px solid var(--icon-ring);
  }
  .popup__body {
    position: absolute;
    left: 118px;
    top: 9px;
    width: 420px;
  }
  .brand {
    display: flex;
    align-items: center;
    gap: 4px;
    height: 16px;
  }
  .brand__dot {
    width: 9px;
    height: 9px;
    border-radius: 50%;
    background: var(--brand-dot);
  }
  .brand__name {
    font-size: 12px;
    font-weight: 500;
    color: var(--text-main);
  }
  .brand__badge {
    margin-left: 5px;
    padding: 1px 5px;
    border-radius: 3px;
    background: var(--badge-bg);
    font-size: 7px;
    font-weight: 700;
    letter-spacing: 0.3px;
    color: var(--text-main);
  }
  .popup__headline {
    margin-top: 5px;
    font-size: 17px;
    font-weight: 500;
    line-height: 20px;
    white-space: nowrap;
  }
  .popup__headline em {
    font-style: normal;
    color: var(--text-accent);
  }
  .popup__sub {
    margin-top: 1px;
    font-size: 11px;
    line-height: 14px;
    color: var(--text-muted);
    white-space: nowrap;
  }
  .popup__cta {
    position: absolute;
    left: 563px;
    top: 34px;
    width: 130px;
    height: 34px;
    border: 1px solid var(--cta-edge);
    border-radius: 2px;
    background: var(--cta-bg);
    color: var(--text-main);
    font-family: inherit;
    font-size: 11px;
    font-weight: 500;
    letter-spacing: 0.2px;
    display: flex;
    align-items: center;
    justify-content: center;
  }
  .popup__close {
    position: absolute;
    right: 9px;
    top: 7px;
    width: 12px;
    height: 12px;
  }
</style>
</head>
<body>
  <main class="stage">
    <section class="popup" aria-label="Korvel email exposure notice">
      <div class="popup__icon" role="img" aria-label="Person silhouette with warning sign"></div>
      <div class="popup__body">
        <div class="brand">
          <span class="brand__dot"></span>
          <span class="brand__name">Korvel</span>
          <span class="brand__badge">FREE</span>
        </div>
        <p class="popup__headline">Is <em>your email</em> already in a data breach?</p>
        <p class="popup__sub">Find out in 30 seconds and see how to remove your exposed data</p>
      </div>
      <button class="popup__cta" type="button">SCAN MY EMAIL</button>
      <svg class="popup__close" viewBox="0 0 12 12" aria-label="Close">
        <path d="M2.5 2.5 L9.5 9.5 M9.5 2.5 L2.5 9.5" stroke="var(--close)" stroke-width="1.4" stroke-linecap="round"/>
      </svg>
    </section>
  </main>
</body>
</html>
```